LABEL DESIGN FOR A NATURAL SKIN CARE LINE

We are looking for a label design for a new natural skin care line that targets the mindfulness and yoga community. We offer a everyday face wash that is derived from natural ingredients and combine it with online yoga classes that will match the intention on the back of the product label. Please make the logo prominent on the front of the bottle, play with horizontal and vertical placement. The product is called “Mellow Rinse”. We like a more modern clean feel.

DERMAVOWE is essentially a natural wellness beauty brand that will fuse into a line of products, a design should be versatile and include the colors in the logo along with whites. The final design should communicate a natural feel that will speak to the yoga community and mindfulness movement.

Target Market(s)

Yogis, fitness community, natural products

Industry/Entity Type

Skin Care Product

Font styles to use
Serif
Decorative

Requirements
Must have
• logo on the front that is prominent, with “MELLOW RINSE” as the product name.

Bottle Dimensions:
3OZ 3.35x4.75in (check attachments)
Nice to have
• Unique designs that stand out. Use the colors in logo. Would be great to have a third eye as a watermark
Should not have
• dark colors,

```html
<!DOCTYPE html>
<html lang="en">
<head>
<meta charset="utf-8">
<title>DERMAVOWE Mellow Rinse – Label</title>
<link href="https://fonts.googleapis.com/css2?family=Montserrat:wght@400;600&family=Raleway:wght@400&display=swap" rel="stylesheet">
<style>
  :root {
    --bg: #e6e6e6;
    --label: #ffffff;
    --teal: #1fb5a8;
    --lime: #8cc63f;
    --band-start: #2fae72;
    --band-end: #8cc63f;
    --ink: #3b3b3b;
    --ink-soft: #555555;
  }
  * { margin: 0; padding: 0; box-sizing: border-box; }
  html, body {
    width: 1200px; height: 972px; overflow: hidden;
    background: var(--bg);
  }
  .canvas {
    position: relative; width: 1200px; height: 972px;
  }
  .label {
    position: absolute;
    background: var(--label);
    display: flex; flex-direction: column; align-items: center;
    border-radius: 6px;
  }
  .label--tube { left: 300px; top: 205px; width: 320px; height: 610px; }
  .label--bottle { left: 656px; top: 335px; width: 180px; height: 470px; }

  .brand {
    display: flex; align-items: center; gap: 8px;
    font-family: "Montserrat", sans-serif; font-weight: 600;
    color: var(--teal);
  }
  .brand__dot {
    border: 2px solid var(--lime); border-radius: 50%;
  }
  .label--tube .brand { margin-top: 120px; font-size: 19px; }
  .label--tube .brand__dot { width: 30px; height: 30px; }
  .label--bottle .brand { margin-top: 100px; font-size: 15px; }
  .label--bottle .brand__dot { width: 24px; height: 24px; }

  .product-tag {
    position: relative;
    font-family: "Raleway", sans-serif; font-weight: 400;
    color: var(--ink-soft); text-align: center;
  }
  .product-tag svg { position: absolute; inset: 0; width: 100%; height: 100%; }
  .label--tube .product-tag { margin-top: 70px; width: 150px; height: 30px; line-height: 30px; font-size: 16px; }
  .label--bottle .product-tag { margin-top: 60px; width: 158px; height: 28px; line-height: 28px; font-size: 15px; }

  .product-name {
    font-family: "Montserrat", sans-serif; font-weight: 600;
    color: var(--ink); letter-spacing: 0.2em;
  }
  .label--tube .product-name { margin-top: 22px; font-size: 18px; }
  .label--bottle .product-name { margin-top: 22px; font-size: 17px; }

  .band { background: linear-gradient(90deg, var(--band-start), var(--band-end)); }
  .label--tube .band { margin-top: 58px; width: 226px; height: 74px; }
  .label--bottle .band { margin-top: 70px; width: 180px; height: 70px; }

  .volume {
    font-family: "Montserrat", sans-serif; font-weight: 400;
    color: var(--ink-soft); font-size: 11px;
  }
  .label--tube .volume { margin-top: 12px; }
  .label--bottle .volume { margin-top: 14px; }
</style>
</head>
<body>
<main class="canvas">
  <section class="label label--tube">
    <div class="brand"><span class="brand__dot"></span>DERMAVOWE</div>
    <div class="product-tag">
      <svg viewBox="0 0 150 30" preserveAspectRatio="none" aria-hidden="true">
        <defs><linearGradient id="frameA" x1="0" x2="1"><stop offset="0" stop-color="#1fb5a8"/><stop offset="1" stop-color="#8cc63f"/></linearGradient></defs>
        <rect x="1" y="1" width="148" height="28" fill="none" stroke="url(#frameA)" stroke-width="2"/>
      </svg>
      MELLOW
    </div>
    <h2 class="product-name">RINSE</h2>
    <div class="band"></div>
    <p class="volume">3OZ</p>
  </section>

  <section class="label label--bottle">
    <div class="brand"><span class="brand__dot"></span>DERMAVOWE</div>
    <div class="product-tag">
      <svg viewBox="0 0 158 28" preserveAspectRatio="none" aria-hidden="true">
        <defs><linearGradient id="frameB" x1="0" x2="1"><stop offset="0" stop-color="#1fb5a8"/><stop offset="1" stop-color="#8cc63f"/></linearGradient></defs>
        <rect x="1" y="1" width="156" height="26" fill="none" stroke="url(#frameB)" stroke-width="2"/>
      </svg>
      MELLOW
    </div>
    <h2 class="product-name">RINSE</h2>
    <div class="band"></div>
    <p class="volume">3OZ</p>
  </section>
</main>
</body>
</html>
```